Professional business cards for real estate development company

I need business cards for my new real estate development company. The company, "KORVA" is a real estate development, investment, and advisory firm with a focus on multifamily, office, and mixed-use projects across primary and secondary markets in the Southeast United States.

Style preference is modern

Industry/Entity Type

Real Estate Development

Contact Information for Business Card

The business cards need to include:
Name
Title
Mailing Address
Phone Number
Web Address

Logo is attached. I would like white to be the primary color with incorporation of the company colors: #232D3A and #B5A451

Font styles to use
Other font styles liked:
• Montserrat, Avenir

Requirements
Must have
• Company Logo. No need to include the company name since the name is in the logo.
Should not have
• No line type designs

```html
<!DOCTYPE html>
<html lang="en">
<head>
<meta charset="utf-8">
<title>KORVA Business Cards</title>
<link href="https://fonts.googleapis.com/css2?family=Nunito+Sans:wght@400;600&display=swap" rel="stylesheet">
<style>
  :root {
    --navy: #232d3a;
    --gold: #b5a451;
    --paper: #e6e6e4;
    --ink-soft: #4a4f57;
    --white: #ffffff;
  }
  html, body {
    margin: 0;
    padding: 0;
    width: 1200px;
    height: 900px;
    overflow: hidden;
    background: var(--gold);
    font-family: "Nunito Sans", "Avenir", sans-serif;
  }
  .canvas {
    position: relative;
    width: 1200px;
    height: 900px;
  }
  .card {
    position: absolute;
    left: 363px;
    width: 475px;
    height: 271px;
  }
  .card-front {
    top: 145px;
    background: var(--navy);
  }
  .card-back {
    top: 484px;
    background: var(--paper);
    color: var(--ink-soft);
  }
  .wordmark {
    position: absolute;
    margin: 0;
    font-weight: 600;
    letter-spacing: 2px;
    line-height: 1;
  }
  .card-front .wordmark {
    right: 28px;
    bottom: 52px;
    font-size: 44px;
    color: var(--white);
  }
  .card-back .wordmark {
    right: 30px;
    bottom: 92px;
    font-size: 34px;
    color: var(--navy);
  }
  .person {
    position: absolute;
    left: 27px;
    top: 64px;
  }
  .person-name {
    margin: 0;
    font-size: 14px;
    font-weight: 400;
    color: var(--navy);
  }
  .person-title {
    margin: 2px 0 0;
    font-size: 11px;
  }
  .contact-list {
    position: absolute;
    left: 27px;
    top: 122px;
    margin: 0;
    padding: 0;
    list-style: none;
    font-size: 11px;
  }
  .contact-list li {
    display: flex;
    align-items: center;
    gap: 6px;
    height: 15px;
  }
  .contact-icon {
    width: 12px;
    height: 12px;
    flex: none;
  }
  .address {
    position: absolute;
    left: 28px;
    top: 172px;
    margin: 0;
    font-size: 11px;
    font-style: normal;
    line-height: 15px;
  }
</style>
</head>
<body>
<main class="canvas">
  <section class="card card-front">
    <p class="wordmark">KORVA</p>
  </section>

  <section class="card card-back">
    <div class="person">
      <h1 class="person-name">Daniel Reyes</h1>
      <p class="person-title">Managing Partner</p>
    </div>
    <ul class="contact-list">
      <li>
        <svg class="contact-icon" viewBox="0 0 12 12" aria-hidden="true">
          <circle cx="6" cy="6" r="6" fill="var(--gold)"/>
          <path d="M3.6 3.2 L4.8 3 L5.4 4.6 L4.7 5.2 Q5.3 6.6 6.8 7.3 L7.4 6.6 L9 7.2 L8.8 8.4 Q5.6 8.6 3.6 3.2 Z" fill="var(--white)"/>
        </svg>
        <span>555-214-0387</span>
      </li>
      <li>
        <svg class="contact-icon" viewBox="0 0 12 12" aria-hidden="true">
          <circle cx="6" cy="6" r="6" fill="var(--gold)"/>
          <rect x="3" y="4" width="6" height="4.2" fill="none" stroke="var(--white)" stroke-width="0.8"/>
          <path d="M3 4 L6 6.4 L9 4" fill="none" stroke="var(--white)" stroke-width="0.8"/>
        </svg>
        <span>danielreyes@korva.com</span>
      </li>
    </ul>
    <address class="address">2180 Oak Avenue, Suite 310,<br>Greenville, SC 29601</address>
    <p class="wordmark">KORVA</p>
  </section>
</main>
</body>
</html>
```